Keystone Draftworks - business cards
A set of business cards for a company
Dear designers,
I suggest that we minimize the quantity of red and grey filled areas on the cards.
I favour more the versions where there is more white space and just some colored accents.
In my opinion it looks more appropriate for our corporate customers.
Thanks for your understanding.
It might be a good idea to print a QR code on the back side of the card if it fits logically.
Not necessary but I'd like to see some ideas with and without it.

```html
<!DOCTYPE html>
<html lang="en">
<head>
<meta charset="utf-8">
<title>Keystone Draftworks – Business Card</title>
<link href="https://fonts.googleapis.com/css2?family=Archivo:wght@400;800&display=swap" rel="stylesheet">
<style>
  :root {
    --backdrop: #e9e6e1;
    --card: #ffffff;
    --brand-red: #c8102e;
    --brand-red-dark: #8e0a1f;
    --brand-red-light: #e23a4f;
    --text-grey: #555555;
    --rule-grey: #d9d9d9;
    --icon-white: #ffffff;
  }
  html, body {
    margin: 0;
    padding: 0;
    width: 1200px;
    height: 852px;
    overflow: hidden;
    background: var(--backdrop);
    font-family: "Archivo", Arial, sans-serif;
  }
  .card {
    position: absolute;
    left: 80px;
    top: 126px;
    width: 1040px;
    height: 600px;
    background: var(--card);
    border-radius: 34px;
    box-shadow: 0 6px 20px rgba(0,0,0,0.18);
    overflow: hidden;
  }
  .accent-band {
    position: absolute;
    left: 70px;
    top: 0;
    width: 84px;
    height: 100%;
    background: linear-gradient(90deg, var(--brand-red-dark) 0%, var(--brand-red) 35%, var(--brand-red-light) 55%, var(--brand-red) 75%, var(--brand-red-dark) 100%);
  }
  .accent-band::before,
  .accent-band::after {
    content: "";
    position: absolute;
    top: 0;
    width: 3px;
    height: 100%;
    background: var(--rule-grey);
  }
  .accent-band::before { left: -7px; }
  .accent-band::after { right: -7px; }
  .brand-mark {
    position: absolute;
    left: 88px;
    top: 62px;
    width: 48px;
    height: 48px;
    border-radius: 50%;
    background: var(--card);
  }
  .brand-name {
    position: absolute;
    left: 172px;
    top: 46px;
    margin: 0;
    color: var(--brand-red);
    font-weight: 800;
    line-height: 1;
    text-transform: uppercase;
  }
  .brand-name .line-main {
    display: block;
    font-size: 70px;
    letter-spacing: -1px;
  }
  .brand-name .line-sub {
    display: block;
    font-size: 34px;
    letter-spacing: 6px;
    text-align: right;
    margin-top: 6px;
  }
  .contact {
    position: absolute;
    left: 182px;
    top: 300px;
    color: var(--text-grey);
    font-size: 21px;
    line-height: 29.4px;
  }
  .contact .address { margin-bottom: 22px; }
  .contact p { margin: 0; }
  .contact-icons {
    position: absolute;
    left: 96px;
    top: 382px;
  }
  .contact-icons svg {
    display: block;
    width: 26px;
    height: 26px;
    margin-bottom: 3.4px;
  }
  .person {
    position: absolute;
    right: 96px;
    top: 306px;
    text-align: right;
  }
  .person .name {
    margin: 0;
    color: var(--brand-red);
    font-weight: 800;
    font-size: 30px;
  }
  .person .role {
    margin: 6px 0 0;
    color: var(--text-grey);
    font-size: 20px;
  }
</style>
</head>
<body>
  <article class="card">
    <div class="accent-band"></div>
    <span class="brand-mark"></span>
    <h1 class="brand-name">
      <span class="line-main">Keystone</span>
      <span class="line-sub">Draftworks</span>
    </h1>

    <div class="contact">
      <div class="address">
        <p>Alder Lane, 14</p>
        <p>Brookfield, 40512</p>
      </div>
      <p>+1 555 201-8842</p>
      <p>+1 555 418-2297</p>
      <p>+1 555 630-5173</p>
      <p>t.vernon@keystonedw.com</p>
      <p>www.keystonedw.com</p>
    </div>

    <div class="contact-icons" aria-hidden="true">
      <svg viewBox="0 0 24 24"><path fill="var(--icon-white)" d="M7 3h4l1 5-2.5 1.5a11 11 0 0 0 5 5L16 12l5 1v4a2 2 0 0 1-2 2A16 16 0 0 1 5 5a2 2 0 0 1 2-2z"/></svg>
      <svg viewBox="0 0 24 24"><rect x="7" y="2" width="10" height="20" rx="2" fill="var(--icon-white)"/><rect x="9" y="5" width="6" height="11" fill="var(--brand-red)"/></svg>
      <svg viewBox="0 0 24 24"><rect x="4" y="8" width="16" height="11" rx="1" fill="var(--icon-white)"/><rect x="7" y="3" width="10" height="6" fill="var(--icon-white)"/><rect x="7" y="14" width="10" height="3" fill="var(--brand-red)"/></svg>
      <svg viewBox="0 0 24 24"><rect x="3" y="6" width="18" height="13" rx="1" fill="var(--icon-white)"/><path d="M3 7l9 7 9-7" stroke="var(--brand-red)" stroke-width="2" fill="none"/></svg>
      <svg viewBox="0 0 24 24"><circle cx="12" cy="12" r="9" fill="none" stroke="var(--icon-white)" stroke-width="2"/><path d="M3 12h18M12 3c-4 5-4 13 0 18M12 3c4 5 4 13 0 18" stroke="var(--icon-white)" stroke-width="1.6" fill="none"/></svg>
    </div>

    <div class="person">
      <p class="name">Tobias Vernon</p>
      <p class="role">Director</p>
    </div>
  </article>
</body>
</html>
```